Math Word Problems Make Your Palms Sweat??

I need a landing page for lead magnet download and email capture. Prospects will get here from QV ad. Landing page should be clean, simple and aimed at parents of Algebra 1 students. I will attach logo. Please use logo brand colors and fonts. The final design should be clear, easy to understand with struggling students and parents that don't know how to help. Copy should include: (lead magnet download info:) Equation Riddle Rescue Bundle with examples AND solutions, Conquer word problems with a step by step guide written by former teacher and full time math tutor.

Target Market(s)

Parents of struggling high school math/Algebra 1 students

Colors
33b8a4
ffffff

Requirements
Must have
• address pain points of:
struggling students
word problems causing angst
parents not knowing how to help their child

be clean, simple and easy to see what my message is via copy, images and feel of page

brand colors (ffffff, 5f5e60, 00a99d)and fonts (questrial, glacial indifference and arimo) from attached logo

clear call to action (download the pdf/lead magnet)
Nice to have
• bulleted points, not too wordy but clear message

related images/teens/struggling with math

my headshot if it looks appropriate on page

(I will likely have revisions once I see the first draft)
Should not have
• crowded
hard to read
message hard to decipher
busy
unclear call to action

```html
<!DOCTYPE html>
<html lang="en">
<head>
<meta charset="utf-8">
<title>Clearpath Tutoring – Equation Riddle Rescue Bundle</title>
<link href="https://fonts.googleapis.com/css2?family=Questrial&family=Open+Sans:wght@400;600&display=swap" rel="stylesheet">
<style>
:root{
  --teal:#00a99d;
  --slate:#5f5e60;
  --paper:#f3f3f3;
  --white:#ffffff;
  --ink:#555557;
  --line:#c9c9c9;
}
*{box-sizing:border-box;margin:0;padding:0}
html,body{width:1200px;height:1109px;overflow:hidden;background:var(--white);font-family:"Open Sans",sans-serif;color:var(--ink)}
.page{position:relative;width:1200px;height:1109px}
.hero{position:absolute;left:0;top:0;width:1200px;height:576px}
.hero-panel{position:absolute;left:0;top:0;width:600px;height:576px;background:var(--paper)}
.hero-photo{position:absolute;left:600px;top:0;width:600px;height:576px;background:linear-gradient(120deg,#d9d6dc 0%,#c7b7cf 35%,#b99aa9 60%,#e2d3cc 100%)}
.accent-dark{position:absolute;left:576px;top:0;width:24px;height:154px;background:var(--slate)}
.accent-teal{position:absolute;left:600px;top:154px;width:24px;height:422px;background:var(--teal)}
.brand{position:absolute;left:144px;top:70px;width:320px}
.brand-name{display:flex;align-items:center;gap:10px;white-space:nowrap;font-family:"Questrial",sans-serif;font-size:34px;line-height:1;color:var(--teal)}
.brand-mark{width:18px;height:18px;background:var(--slate)}
.brand-tag{margin-top:16px;font-family:"Questrial",sans-serif;font-size:17px;line-height:1;color:var(--slate)}
.headline{position:absolute;left:144px;top:206px;width:440px;font-family:"Questrial",sans-serif;font-weight:400;font-size:27px;line-height:35px;color:var(--teal)}
.signup{position:absolute;left:144px;top:294px;width:224px}
.field{display:block;width:224px;height:43px;border:1px solid #c4c4c4;background:var(--white);padding:0 15px;font-family:"Open Sans",sans-serif;font-size:13px;color:#666;margin-bottom:9px}
.privacy{margin-top:7px;font-size:10.5px;line-height:16px;color:#555}
.cta{display:block;margin-top:6px;width:224px;height:62px;border:0;background:var(--teal);color:var(--white);font-family:"Questrial",sans-serif;font-size:17px;line-height:22px}
.tutor{position:absolute;left:400px;top:294px;width:160px;text-align:center}
.tutor-photo{width:160px;height:190px;background:linear-gradient(160deg,#b9b5ae,#e6e2dc 55%,#cfc9c0)}
.tutor-name{margin-top:6px;font-family:"Questrial",sans-serif;font-size:17px;color:var(--teal)}
.tutor-role{font-size:10px;color:#555;margin-top:1px}
.quote{position:absolute;border:1px solid var(--line);border-bottom:0;background:var(--white);font-size:13px;color:#555}
.quote p{position:relative}
.quote-bar{position:absolute;left:-1px;bottom:-8px;right:-1px;height:8px}
.quote-bar .teal{position:absolute;right:0;top:-8px;height:8px;background:var(--teal)}
.quote-bar .dark{position:absolute;left:0;top:0;height:8px;background:var(--slate)}
.quote-author{position:absolute;font-size:16.5px;font-weight:600;color:var(--teal)}
.q1{left:144px;top:618px;width:440px;height:346px;padding:26px 21px;line-height:27.2px}
.q2{left:615px;top:618px;width:440px;height:139px;padding:26px 28px;line-height:24px}
.q3{left:615px;top:826px;width:440px;height:138px;padding:26px 28px;line-height:24px}
.footer{position:absolute;left:0;top:1045px;width:1200px;height:64px;background:var(--slate);color:var(--white)}
.copyright{position:absolute;left:144px;top:24px;font-size:12px}
.social{position:absolute;right:144px;top:20px;display:flex;gap:16px;font-family:"Questrial",sans-serif;font-size:15px}
</style>
</head>
<body>
<div class="page">
  <section class="hero">
    <div class="hero-panel"></div>
    <div class="hero-photo" role="img" aria-label="Photo of a frustrated teen student holding her head over homework while a parent talks with her, with math symbols floating above"></div>
    <div class="accent-dark"></div>
    <div class="accent-teal"></div>

    <div class="brand">
      <div class="brand-name"><span class="brand-mark"></span>Clearpath Tutoring</div>
      <div class="brand-tag">Patient help for every student</div>
    </div>

    <h1 class="headline">Free Equation Riddle Rescue Bundle with Examples and Solutions PDF</h1>

    <form class="signup">
      <input class="field" type="text" placeholder="First Name">
      <input class="field" type="email" placeholder="Email Address">
      <p class="privacy">We hate spam as much as you do.<br>Your email address will never be shared or sold.</p>
      <button class="cta" type="button">I want to CONQUER<br>word problems!</button>
    </form>

    <div class="tutor">
      <div class="tutor-photo" role="img" aria-label="Headshot of the tutor"></div>
      <div class="tutor-name">Dana Whitfield</div>
      <div class="tutor-role">Math Tutor/Teacher</div>
    </div>
  </section>

  <article class="quote q1">
    <p>"I had been feeling frustrated and lost in how to help my two kids with Math and Algebra.&nbsp; Not having a “math brain” of my own, I knew I needed to call in the reinforcements.&nbsp; Enter Dana Whitfield.&nbsp; She is not only extremely knowledgeable but she is patient and genuinely cares about each child she works with.&nbsp; We have seen so much improvement in our kids and their confidence levels in math.&nbsp; There aren’t as many tears anymore . . . and I’m talking about my own . . . with regard to working with them as I have the best teacher guiding all of us each step of the way."</p>
    <div class="quote-bar"><span class="teal" style="width:299px"></span><span class="dark" style="width:141px"></span></div>
  </article>
  <div class="quote-author" style="left:144px;top:986px">~ Marla Jensen</div>

  <article class="quote q2">
    <p>" Eli looks forward to his tutoring with Dana each week. He has shown so much improvement in math. We really appreciate Dana for that. "</p>
    <div class="quote-bar"><span class="teal" style="width:284px"></span><span class="dark" style="width:157px"></span></div>
  </article>
  <div class="quote-author" style="left:615px;top:778px">~ Nora, Eli's mom</div>

  <article class="quote q3">
    <p>"Dana was so helpful in teaching my son Owen how to understand the basics of fractions. She really made it a fun experience for him. We're both very thankful we met with her and will continue tutoring with her. “</p>
    <div class="quote-bar"><span class="teal" style="width:252px"></span><span class="dark" style="width:189px"></span></div>
  </article>
  <div class="quote-author" style="left:615px;top:986px">~ Tessa, Owen's mom</div>

  <footer class="footer">
    <p class="copyright">Copyright &copy; 2020 &nbsp;Clearpath Tutoring. &nbsp;All rights reserved.</p>
    <nav class="social"><span>QV</span><span>Snapline</span></nav>
  </footer>
</div>
</body>
</html>
```